Modern Billboard Ad for Criminal Defense Firm

10.5 x 36 We're looking for something to set us apart from the local competition. Looking for sleek and modern. We're a mid-sized firm in a small market city. We want to give the artist room to be creative on this one.
Thanks

Target Market(s)

Adult clients who have been charged with a crime/DWI

Industry/Entity Type

legal

Font styles to use
Serif
Sans Serif

Requirements
Must have
• Needs to have the firm name in large lettering. Law Offices of Marcus T Whitfield. “PLLC” does not have to be included. Phone number of (555) 384-1927 should be included but not the main focus.
Nice to have
• A call to action or something similar. “Don’t go it alone, call today.”, “ Arrested?”

```html
<!DOCTYPE html>
<html lang="en">
<head>
<meta charset="utf-8">
<title>Arrested? – Law Offices of Marcus T Whitfield Billboard</title>
<link rel="stylesheet" href="https://fonts.googleapis.com/css2?family=Bebas+Neue&family=Libre+Baskerville&family=Montserrat:wght@700&display=swap">
<style>
  :root {
    --page: #eceaea;
    --ink: #000000;
    --white: #ffffff;
    --gold: #f7c300;
    --red: #e3161f;
    --badge: #1e8fc8;
  }
  * { margin: 0; padding: 0; box-sizing: border-box; }
  html, body { width: 1200px; height: 1192px; overflow: hidden; background: var(--page); }
  .billboard {
    position: absolute; left: 40px; top: 433px;
    width: 1120px; height: 326px;
    background: var(--ink); overflow: hidden;
  }
  .photo-cuffs {
    position: absolute; left: 0; top: 0; width: 420px; height: 100%;
    background:
      linear-gradient(90deg, rgba(0,0,0,0) 55%, #000 100%),
      radial-gradient(ellipse at 40% 55%, #a9606a 0%, #6e3a40 40%, #2a1a1c 80%);
  }
  .photo-attorney {
    position: absolute; right: 0; top: 0; width: 240px; height: 100%;
    background: linear-gradient(90deg, #000 0%, #3a3a3a 30%, #8a8a8a 60%, #5a5a5a 100%);
  }
  .headline {
    position: absolute; left: 378px; top: 26px; width: 542px;
    font-family: "Bebas Neue", sans-serif; font-size: 152px; line-height: 1;
    letter-spacing: 1px; text-align: center;
    background: linear-gradient(180deg, var(--white) 45%, var(--gold) 95%);
    -webkit-background-clip: text; background-clip: text; color: transparent;
  }
  .cta-band {
    position: absolute; left: 447px; top: 150px; width: 390px; height: 30px;
    background: var(--red); transform: rotate(-1.8deg);
    font-family: "Libre Baskerville", serif; font-size: 18px; line-height: 30px;
    color: var(--white); text-align: center; white-space: nowrap;
  }
  .cta-band .accent { color: var(--gold); }
  .divider {
    position: absolute; left: 553px; top: 205px; width: 155px; height: 2px; background: var(--white);
  }
  .divider::after {
    content: ""; position: absolute; left: 32px; top: -1px; width: 90px; height: 4px; background: var(--white);
  }
  .firm-name {
    position: absolute; left: 360px; top: 226px; width: 580px;
    font-family: "Bebas Neue", sans-serif; font-size: 54px; line-height: 1;
    color: var(--white); text-align: center; white-space: nowrap;
  }
  .firm-name .accent { color: var(--gold); }
  .contact {
    position: absolute; left: 360px; top: 280px; width: 580px;
    font-family: "Montserrat", sans-serif; font-weight: 700; font-size: 18px;
    color: var(--white); text-align: center; white-space: nowrap;
  }
  .contact .dash { color: var(--gold); }
  .contact .sep { display: inline-block; width: 1px; height: 20px; background: var(--white); vertical-align: -4px; margin: 0 8px; }
  .award-badge {
    position: absolute; left: 1052px; top: 240px; width: 56px; height: 74px;
    background: var(--badge); border: 2px solid var(--white);
  }
</style>
</head>
<body>
  <div class="billboard">
    <div class="photo-cuffs" role="img" aria-label="Close-up photo of hands in handcuffs behind a person's back"></div>
    <div class="photo-attorney" role="img" aria-label="Black and white portrait of the attorney in a vest and tie with a jacket over his shoulder"></div>
    <h1 class="headline">ARRESTED?</h1>
    <p class="cta-band">DON’T GO IT ALONE, <span class="accent">CALL TODAY</span></p>
    <div class="divider"></div>
    <h2 class="firm-name"><span class="accent">LAW OFFICES OF</span> MARCUS T WHITFIELD</h2>
    <p class="contact"><span class="dash">—</span> (555) 384-1927<span class="sep"></span>www.mwhitfieldlaw.com <span class="dash">—</span></p>
    <div class="award-badge" aria-hidden="true"></div>
  </div>
</body>
</html>
```